I’m looking for a vibrant, eye-catching package design for our new premium cannabis gummies, GLIMMER. This is a high-end cannabis edible gummy made with real fruit, vegan ingredients, and powered by a THC nano emulsion — the most effective way to ingest cannabis. The package will be a square-bottom bag with child-resistant zippers (image of bag attached).

What we want from you? We want your version of what the front of the bag should look like.

The following text elements should be included within your vision of the bag

Glimmer - Premium Cannabis Gummy
10 pieces per bag | 10mg THC per piece | 100mg THC total
Made with real fruit
Vegan (include a vegan symbol)
Flavors: Assorted flavors (Strawberry, Mango, Pineapple, Orange, Blueberry)
Oregon cannabis icon (attached)
Net Weight 250 grams (bottom of bag)

What is needed after you win.
2 other sizes. Same look but will need to rearrange some elements of the bag. The back of the bag will be the same for all sizes. Will be legal text and nutritional info. Larger two sizes has sides, as per the attached bag. All sizes will have a bottom as well. the first size will have 5 versions for flavors. Other 2 sizes will be 1 design with "assorted flavors".

Target Market(s)

Cannabis market in Oregon

Industry/Entity Type

cannabis

Requirements
Must have
• the Marijuana universal icon for being a cannabis product.
Nice to have
• nice images of fruits
Should not have
• graphic, cartoon images that would appeal to minors.

```html
<!DOCTYPE html>
<html lang="en">
<head>
<meta charset="utf-8">
<title>Glimmer Premium Cannabis Gummy – Bag Front</title>
<link rel="stylesheet" href="https://fonts.googleapis.com/css2?family=Lato:wght@400;700&family=Allura&display=swap">
<style>
  :root {
    --page: #fefbeb;
    --bag: #ffffff;
    --bag-edge: #d9d9d9;
    --ink: #111111;
    --bar: #333333;
    --script: #666666;
    --green-dark: #3f8a2f;
    --green-mid: #8cc63f;
    --green-light: #b3d97a;
    --red: #c41e00;
    --orange: #e0901e;
    --yellow: #f5d400;
    --pink: #dc5a7f;
    --blue: #6a7dbb;
    --cannabis-red: #d6202f;
  }
  html, body {
    margin: 0;
    padding: 0;
    width: 1200px;
    height: 1000px;
    overflow: hidden;
    background: var(--page);
  }
  .canvas { display: block; width: 1200px; height: 1000px; }
  .bag-face { fill: var(--bag); stroke: var(--bag-edge); stroke-width: 1; }
  .fold-line { stroke: var(--bag-edge); stroke-width: 1; }
  .view-label { font-family: "Lato", sans-serif; font-size: 13px; fill: var(--ink); }
  .brand-name { font-family: "Lato", sans-serif; font-weight: 700; fill: #ffffff; letter-spacing: 1px; }
  .brand-dot { fill: #ffffff; }
  .tier-bar { fill: var(--bar); }
  .tier-text { font-family: "Lato", sans-serif; fill: #ffffff; letter-spacing: 3px; }
  .product-name { font-family: "Lato", sans-serif; fill: var(--ink); }
  .tagline { font-family: "Allura", cursive; fill: var(--script); }
  .flavor-text { font-family: "Lato", sans-serif; fill: #ffffff; }
  .dose-text, .weight-text { font-family: "Lato", sans-serif; fill: var(--ink); }
  .vegan-badge { fill: #ffffff; stroke: var(--ink); }
  .cannabis-badge-frame { fill: var(--ink); }
  .cannabis-badge-field { fill: var(--cannabis-red); }
</style>
</head>
<body>
<svg class="canvas" viewBox="0 0 1200 1000" xmlns="http://www.w3.org/2000/svg">
  <defs>
    <linearGradient id="greenSweep" x1="0" y1="1" x2="1" y2="0">
      <stop offset="0" stop-color="var(--green-dark)"/>
      <stop offset="0.45" stop-color="var(--green-mid)"/>
      <stop offset="1" stop-color="var(--green-light)"/>
    </linearGradient>
    <linearGradient id="flavorSweep" x1="0" y1="1" x2="1" y2="0">
      <stop offset="0" stop-color="var(--blue)"/>
      <stop offset="0.55" stop-color="var(--pink)"/>
      <stop offset="1" stop-color="var(--yellow)"/>
    </linearGradient>
    <linearGradient id="fruitTones" x1="0" y1="0" x2="1" y2="1">
      <stop offset="0" stop-color="var(--red)" stop-opacity="0.75"/>
      <stop offset="0.3" stop-color="var(--orange)" stop-opacity="0.75"/>
      <stop offset="0.5" stop-color="var(--yellow)" stop-opacity="0.75"/>
      <stop offset="0.7" stop-color="var(--green-mid)" stop-opacity="0.75"/>
      <stop offset="1" stop-color="var(--blue)" stop-opacity="0.75"/>
    </linearGradient>
    <clipPath id="largeFaceClip"><rect x="103" y="94" width="537" height="816"/></clipPath>
    <clipPath id="gussetClip"><rect x="702" y="245" width="435" height="482"/></clipPath>
  </defs>

  <!-- Large bag front -->
  <g class="bag bag--large">
    <rect class="bag-face" x="103" y="94" width="537" height="816"/>
    <g clip-path="url(#largeFaceClip)">
      <circle class="brand-accent" cx="146" cy="229" r="148" fill="url(#greenSweep)" role="img" aria-label="Green brand decoration"/>
      <circle class="brand-accent" cx="114" cy="719" r="174" fill="url(#greenSweep)" role="img" aria-label="Green brand decoration"/>
    </g>

    <g class="brand-lockup">
      <circle class="brand-dot" cx="124" cy="219" r="6"/>
      <text class="brand-name" x="136" y="229" font-size="27">GLIMMER</text>
    </g>

    <rect class="tier-bar" x="353" y="173" width="287" height="48"/>
    <text class="tier-text" x="495" y="211" font-size="34" text-anchor="middle">PREMIUM</text>
    <text class="product-name" x="571" y="273" font-size="43" text-anchor="end">Cannabis</text>
    <text class="product-name" x="571" y="329" font-size="43" text-anchor="end">Gummy</text>

    <rect class="fruit-splash" x="151" y="348" width="390" height="274" rx="137" fill="url(#fruitTones)" role="img" aria-label="Colourful splash illustration of real fruit"/>

    <text class="tagline" x="298" y="704" font-size="40" transform="rotate(-18 298 704)">Made with real fruit</text>

    <path class="flavor-swoosh" d="M337,714 C420,722 500,700 560,676 C600,660 622,690 612,718 C600,760 560,782 520,780 C450,778 390,752 337,714 Z" fill="url(#flavorSweep)"/>
    <g class="flavor-list" transform="rotate(-12 520 728)">
      <text class="flavor-text" x="540" y="710" font-size="15" text-anchor="middle">Assorted flavors</text>
      <text class="flavor-text" x="508" y="729" font-size="15" text-anchor="middle">Strawberry | Mango | Orange,</text>
      <text class="flavor-text" x="528" y="748" font-size="15" text-anchor="middle">Pineapple | Blueberry</text>
    </g>

    <text class="dose-text" x="260" y="807" font-size="17">10 pieces per bag | 10mg THC per piece</text>
    <text class="dose-text" x="260" y="829" font-size="17">100mg THC total</text>
    <text class="weight-text" x="258" y="884" font-size="14">Net Weight 250 grams</text>

    <circle class="vegan-badge" cx="489" cy="866" r="23" stroke-width="4" role="img" aria-label="Vegan badge"/>
    <g class="cannabis-badge" role="img" aria-label="Universal cannabis product badge">
      <rect class="cannabis-badge-frame" x="526" y="843" width="65" height="47" rx="5"/>
      <rect class="cannabis-badge-field" x="550" y="847" width="37" height="39"/>
    </g>
  </g>

  <!-- Medium bag, side gusset and front -->
  <g class="bag bag--gusseted">
    <text class="view-label" x="743" y="230" text-anchor="middle">Side</text>
    <text class="view-label" x="991" y="230" text-anchor="middle">Front</text>

    <rect class="bag-face" x="702" y="245" width="435" height="482"/>
    <g clip-path="url(#gussetClip)">
      <circle class="brand-accent" cx="848" cy="340" r="108" fill="url(#greenSweep)" role="img" aria-label="Green brand decoration"/>
      <circle class="brand-accent" cx="812" cy="616" r="102" fill="url(#greenSweep)" role="img" aria-label="Green brand decoration"/>
    </g>
    <line class="fold-line" x1="824" y1="245" x2="824" y2="727"/>

    <g class="brand-lockup">
      <circle class="brand-dot" cx="862" cy="328" r="3.5"/>
      <text class="brand-name" x="869" y="333" font-size="14">GLIMMER</text>
    </g>

    <rect class="tier-bar" x="969" y="298" width="168" height="28"/>
    <text class="tier-text" x="1052" y="320" font-size="19" text-anchor="middle" letter-spacing="2">PREMIUM</text>
    <text class="product-name" x="1096" y="355" font-size="24" text-anchor="end">Cannabis</text>
    <text class="product-name" x="1096" y="388" font-size="24" text-anchor="end">Gummy</text>

    <rect class="fruit-splash" x="862" y="410" width="208" height="146" rx="73" fill="url(#fruitTones)" role="img" aria-label="Colourful splash illustration of real fruit"/>

    <text class="tagline" x="938" y="607" font-size="23" transform="rotate(-18 938 607)">Made with real fruit</text>

    <path class="flavor-swoosh" d="M960,614 C1010,620 1060,602 1095,589 C1118,580 1126,600 1118,618 C1108,642 1082,652 1058,650 C1020,648 990,636 960,614 Z" fill="url(#flavorSweep)"/>
    <g class="flavor-list" transform="rotate(-12 1060 622)">
      <text class="flavor-text" x="1077" y="612" font-size="8.5" text-anchor="middle">Assorted flavors</text>
      <text class="flavor-text" x="1058" y="623" font-size="8.5" text-anchor="middle">Strawberry | Mango | Orange,</text>
      <text class="flavor-text" x="1070" y="634" font-size="8.5" text-anchor="middle">Pineapple | Blueberry</text>
    </g>

    <text class="dose-text" x="915" y="666" font-size="9.5">10 pieces per bag | 10mg THC per piece</text>
    <text class="dose-text" x="915" y="679" font-size="9.5">100mg THC total</text>
    <text class="weight-text" x="914" y="711" font-size="7.5">Net Weight 250 grams</text>

    <circle class="vegan-badge" cx="1048" cy="701" r="13" stroke-width="2.5" role="img" aria-label="Vegan badge"/>
    <g class="cannabis-badge" role="img" aria-label="Universal cannabis product badge">
      <rect class="cannabis-badge-frame" x="1069" y="688" width="39" height="27" rx="3"/>
      <rect class="cannabis-badge-field" x="1083" y="690" width="23" height="23"/>
    </g>
  </g>
</svg>
</body>
</html>
```